Modern and Improved business card design for Family Dental Practice

We have 2 sets of logo we have designed and now just need a business card layout and design for the office. Colors are on the logo. We can choose which logo we want to go with . The font can be changed to whatever seems modern and relevant. We are family dental office that has been open for over 15 years in South Austin Texas.

Target Market(s)

Handout Business cards to referrals and specialists

Industry/Entity Type

Dental

Contact Information for Business Card

We need address, phone, website and email address. 4830 North Maple Loop Suite 208 , Austin,Texas 78392....phone: 512-847-3195.....email- info@bluepinedental.example....website - BluePineDental.example

Font styles to use
Serif
Decorative

Requirements
Must have
• my logo. We have 2 logos, but we can use just one or if we can incorporate one on one side and the other on the other side.
Nice to have
• Really just need a modern look and clean that incorporates the logo and colors .

```html
<!DOCTYPE html>
<html lang="en">
<head>
<meta charset="utf-8">
<title>Blue Pine Family Dentistry – Business Card</title>
<link href="https://fonts.googleapis.com/css2?family=Questrial&display=swap" rel="stylesheet">
<style>
  :root {
    --backdrop: #2a2a2a;
    --card-black: #1c1c1c;
    --brand-green: #0a7305;
    --leaf-green: #8fa83a;
    --pale-green: #e3ead0;
    --paper: #ffffff;
    --ink: #1a1a1a;
    --emboss: #151515;
  }
  * { box-sizing: border-box; margin: 0; padding: 0; }
  html, body { width: 1200px; height: 1015px; overflow: hidden; }
  body {
    background: var(--backdrop);
    font-family: "Questrial", sans-serif;
    position: relative;
  }
  .card {
    position: absolute;
    left: 250px;
    width: 700px;
    height: 400px;
    overflow: hidden;
    box-shadow: 0 14px 30px rgba(0,0,0,.45);
  }
  .card--front { top: 70px; background: var(--card-black); }
  .card--back { top: 540px; background: var(--card-black); }

  .emboss-mark {
    position: absolute;
    right: 70px;
    top: 60px;
    width: 250px;
    height: 250px;
    border-radius: 50%;
    border: 34px solid var(--emboss);
  }
  .wordmark {
    position: absolute;
    color: var(--paper);
    text-transform: uppercase;
    line-height: 1;
    font-weight: 400;
  }
  .wordmark__name { display: block; font-size: 54px; letter-spacing: 2px; }
  .wordmark__tag { display: block; font-size: 19px; letter-spacing: 5px; margin-top: 10px; }
  .card--front .wordmark { left: 60px; top: 210px; }

  .back-brand { position: absolute; top: 40px; left: 150px; display: flex; align-items: center; gap: 34px; }
  .back-brand__dot { width: 100px; height: 100px; border-radius: 50%; background: var(--brand-green); }
  .back-brand .wordmark { position: static; }
  .back-brand .wordmark__name { font-size: 44px; }
  .back-brand .wordmark__tag { font-size: 15px; letter-spacing: 4px; margin-top: 8px; }

  .contact-band {
    position: absolute; top: 185px; left: 0; right: 0; height: 115px;
    background: var(--brand-green); color: var(--paper);
    display: flex; align-items: center; font-size: 19px; letter-spacing: .5px;
  }
  .contact-band__col { flex: 1; display: flex; flex-direction: column; gap: 10px; }
  .contact-band__col--left { align-items: flex-end; padding-right: 26px; }
  .contact-band__col--right { padding-left: 26px; }
  .contact-band__divider { width: 1px; align-self: stretch; margin: 14px 0; background: rgba(255,255,255,.6); }
  .contact-line { display: flex; align-items: center; gap: 10px; }
  .contact-line svg { width: 18px; height: 18px; fill: var(--paper); flex: none; }
  .address { display: flex; gap: 10px; align-items: flex-start; }
  .address svg { width: 16px; height: 22px; fill: var(--paper); margin-top: 2px; flex: none; }

  .web-strip {
    position: absolute; top: 300px; left: 0; right: 0; height: 80px;
    background: var(--paper); color: var(--ink);
    display: flex; align-items: center; justify-content: center;
    font-size: 24px; letter-spacing: 1px;
  }
  .base-bar { position: absolute; bottom: 0; left: 0; right: 0; height: 20px; display: flex; }
  .base-bar__solid { flex: 0 0 55%; background: var(--brand-green); }
  .base-bar__fade { flex: 1; background: linear-gradient(90deg, var(--leaf-green), var(--pale-green)); }
</style>
</head>
<body>
  <section class="card card--front" aria-label="Card front">
    <div class="emboss-mark" aria-hidden="true"></div>
    <div class="wordmark">
      <span class="wordmark__name">Blue Pine</span>
      <span class="wordmark__tag">Family Dentistry</span>
    </div>
  </section>

  <section class="card card--back" aria-label="Card back">
    <div class="back-brand">
      <div class="back-brand__dot" aria-hidden="true"></div>
      <div class="wordmark">
        <span class="wordmark__name">Blue Pine</span>
        <span class="wordmark__tag">Family Dentistry</span>
      </div>
    </div>

    <div class="contact-band">
      <div class="contact-band__col contact-band__col--left">
        <div class="contact-line">
          <span>512-847-3195</span>
          <svg viewBox="0 0 24 24" aria-hidden="true"><path d="M6.6 10.8a15 15 0 0 0 6.6 6.6l2.2-2.2a1 1 0 0 1 1-.25 11.4 11.4 0 0 0 3.6.57 1 1 0 0 1 1 1V20a1 1 0 0 1-1 1A17 17 0 0 1 3 4a1 1 0 0 1 1-1h3.5a1 1 0 0 1 1 1c0 1.25.2 2.45.57 3.57a1 1 0 0 1-.25 1z"/></svg>
        </div>
        <div class="contact-line">
          <span>info@bluepinedental.example</span>
          <svg viewBox="0 0 24 24" aria-hidden="true"><path d="M2 5h20v14H2zm2 2v.5l8 5 8-5V7zm0 2.8V17h16V9.8l-8 5z"/></svg>
        </div>
      </div>
      <div class="contact-band__divider"></div>
      <div class="contact-band__col contact-band__col--right">
        <div class="address">
          <svg viewBox="0 0 16 22" aria-hidden="true"><path d="M8 0a8 8 0 0 0-8 8c0 6 8 14 8 14s8-8 8-14a8 8 0 0 0-8-8zm0 11a3 3 0 1 1 0-6 3 3 0 0 1 0 6z"/></svg>
          <span>4830 North Maple Loop<br>Suite 208 Austin Texas 78392</span>
        </div>
      </div>
    </div>

    <div class="web-strip">BluePineDental.example</div>
    <div class="base-bar" aria-hidden="true">
      <div class="base-bar__solid"></div>
      <div class="base-bar__fade"></div>
    </div>
  </section>
</body>
</html>
```